Stationery Design needed for logo design project

This project is linked to Logo: brand identity for modern furniture design studio..

Our company needs a Stationery Design. Please refer to our original project in the link above.

```html
<!DOCTYPE html>
<html lang="en">
<head>
<meta charset="utf-8">
<title>ferrow — Business Cards</title>
<link rel="stylesheet" href="https://fonts.googleapis.com/css2?family=Questrial&family=Montserrat:wght@700&display=swap">
<style>
  :root {
    --canvas-bg: #e4e4e4;
    --card-white: #fbfbfb;
    --card-dark-top: #3c3c3c;
    --card-dark-bottom: #575757;
    --ink-logo: #555555;
    --ink-logo-light: #e2e2e2;
    --ink-text: #4a4a4a;
    --ink-muted: #6d6d6d;
    --rule: #cfcfcf;
  }
  * { box-sizing: border-box; margin: 0; padding: 0; }
  html, body {
    width: 1200px;
    height: 900px;
    overflow: hidden;
    background: var(--canvas-bg);
  }
  .sheet {
    width: 1200px;
    height: 900px;
    display: flex;
    flex-direction: column;
    align-items: center;
    justify-content: center;
    gap: 56px;
  }
  .card {
    width: 560px;
    height: 340px;
    position: relative;
    box-shadow: 0 6px 18px rgba(0, 0, 0, 0.18);
  }
  .card--back {
    background: linear-gradient(160deg, var(--card-dark-top), var(--card-dark-bottom));
    display: flex;
    align-items: center;
    justify-content: center;
  }
  .card--front {
    background: var(--card-white);
    display: flex;
    flex-direction: column;
    align-items: center;
  }
  .wordmark {
    font-family: "Questrial", sans-serif;
    font-weight: 400;
    letter-spacing: 1px;
    line-height: 1;
  }
  .card--back .wordmark {
    font-size: 64px;
    color: var(--ink-logo-light);
  }
  .card--front .wordmark {
    font-size: 64px;
    color: var(--ink-logo);
    margin-top: 62px;
  }
  .holder {
    margin-top: 52px;
    text-align: center;
  }
  .holder__name {
    font-family: "Montserrat", sans-serif;
    font-weight: 700;
    font-size: 15px;
    letter-spacing: 0.6px;
    text-transform: uppercase;
    color: var(--ink-text);
  }
  .holder__role {
    font-family: "Questrial", sans-serif;
    font-size: 13px;
    color: var(--ink-muted);
    margin-top: 3px;
  }
  .divider {
    width: 400px;
    height: 1px;
    background: var(--rule);
    margin-top: 16px;
  }
  .contact {
    font-family: "Questrial", sans-serif;
    font-size: 11.5px;
    color: var(--ink-muted);
    text-align: center;
    line-height: 1.55;
    margin-top: 12px;
  }
  .contact b {
    font-family: "Montserrat", sans-serif;
    font-weight: 700;
    font-size: 10.5px;
    color: var(--ink-text);
  }
</style>
</head>
<body>
  <main class="sheet">
    <section class="card card--back" aria-label="Card back">
      <span class="wordmark">ferrow</span>
    </section>

    <section class="card card--front" aria-label="Card front">
      <span class="wordmark">ferrow</span>
      <div class="holder">
        <p class="holder__name">Jamie Whitlock</p>
        <p class="holder__role">General Manager</p>
      </div>
      <div class="divider"></div>
      <address class="contact" style="font-style: normal;">
        Unit 4, 27 Marlow St, Ashcroft 4120 · <b>T:</b> (07) 5550 1294<br>
        <b>F:</b> (07) 5550 1295 · <b>E:</b> hello@ferrow.com · www.ferrow.com
      </address>
    </section>
  </main>
</body>
</html>
```